Velvet Amps Poster / Flyer Ad Design

We need a poster design (and a complimentary A6 flyer) to promote our Adult Rock Band Course called 'Velvet Amps'.

Target market is adults aged 25 - 50 primarily

Design to be eye catching, creative, appealing and easy to understand. Most of the distribution will be street marketing, email marketing, social media, music magazines and websites and to other music teachers.

We need the design to be as an A3 and A4 poster and an A6 promo flyer/e-flyer. Should look good in colour and we'll want a version in black and white.

Would be good to also incorporate our music school logo (just for branding purposes).

Text as follows:

VELVET AMPS
The Ultimate Rock Band Course for Adults

Ever wondered what it would be like to play in a band?

Feeling musically rusty and looking for a way to start playing your instrument again?

Then here’s an exciting opportunity you can’t miss!

All musical levels
Beginner/Intermediate to Advanced Players

Limited Numbers

REGISTER ONLINE NOW
www.tunelanestudio.com.au

Starts Saturday 3rd August
Newtown

Over 6 exciting weekends you’ll work with one of our experienced professional band coaches and transform yourselves into the ultimate ‘Velvet Amps’

Discover how to play in a band
Revisit your musical abilities
Practice songs
Perform on Stage

Drummers, Bass Guitarists, Singers, Keys, Guitarists, Saxophone, Percussionists and others all welcome to join

For more information, course costs and registration, please visit www.tunelanestudio.com.au or call 02 7194 2586 / 0472 908 645

Reason: Hi Everyone, I've been away and unable to respond to some of the designs because I've been ill. Have decided to extend the deadline and now commit to paying designers. Look forward to seeing more designs. Any questions, please let me know. Thanks Mirela

```html
<!DOCTYPE html>
<html lang="en">
<head>
<meta charset="utf-8">
<title>Velvet Amps – The Ultimate Rock Band Course for Adults</title>
<link rel="stylesheet" href="https://fonts.googleapis.com/css2?family=Cinzel:wght@400;600;700&family=Open+Sans:wght@600;700;800&display=swap">
<style>
  :root {
    --curtain-red: #d8322a;
    --curtain-orange: #f2702a;
    --stage-magenta: #8a1f5a;
    --stage-violet: #3a1548;
    --night: #0b0710;
    --wood: #4a2f20;
    --title-blue: #4bb3d8;
    --title-deep: #1d6f98;
    --ink-dark: #2a0810;
    --cream: #fbe9e2;
    --white: #ffffff;
    --brand-blue: #3aa7d6;
  }
  * { margin: 0; padding: 0; box-sizing: border-box; }
  html, body { width: 856px; height: 1200px; overflow: hidden; background: var(--night); }
  .poster {
    position: relative; width: 856px; height: 1200px; overflow: hidden;
    font-family: "Cinzel", "Times New Roman", serif; color: var(--white);
  }
  .stage-scene {
    position: absolute; inset: 0;
    background:
      radial-gradient(ellipse 60% 35% at 55% 48%, rgba(255,190,150,0.35), transparent 70%),
      linear-gradient(180deg, var(--curtain-orange) 0%, var(--curtain-red) 22%, #b8284a 40%, var(--stage-magenta) 55%, var(--stage-violet) 68%, var(--night) 80%, #1a0f0c 88%, var(--wood) 100%);
  }
  .line { position: absolute; left: 0; width: 100%; text-align: center; white-space: nowrap; }
  .title {
    top: 18px; font-size: 104px; font-weight: 700; letter-spacing: 2px;
    color: var(--title-blue);
    text-shadow: 0 2px 0 var(--title-deep), 0 0 18px rgba(255,255,255,0.5), 0 4px 10px rgba(0,0,0,0.5);
  }
  .subtitle {
    top: 176px; font-size: 50px; font-weight: 700; color: var(--cream);
    text-shadow: 0 2px 3px rgba(0,0,0,0.7), 0 0 10px rgba(80,20,10,0.6);
  }
  .subtitle-dark {
    top: 240px; font-size: 52px; font-weight: 700; color: var(--ink-dark);
    text-shadow: 0 0 12px rgba(255,255,255,0.9), 0 0 4px rgba(255,255,255,0.8);
  }
  .intro { font-size: 20px; letter-spacing: 1px; color: var(--cream); text-shadow: 0 1px 3px rgba(0,0,0,0.6); }
  .callout { font-size: 31px; font-weight: 700; color: var(--white); text-shadow: 0 2px 4px rgba(0,0,0,0.6); }
  .detail { font-size: 20px; color: var(--white); text-shadow: 0 1px 3px rgba(0,0,0,0.7); }
  .detail-strong { font-size: 22px; font-weight: 700; }
  .detail-large { font-size: 26px; }
  .small { font-size: 15px; letter-spacing: 0.5px; color: var(--white); text-shadow: 0 1px 2px rgba(0,0,0,0.8); }
  .welcome { top: 960px; font-size: 34px; font-weight: 700; letter-spacing: 1px; }
  .register {
    position: absolute; left: 46px; font-family: "Open Sans", Arial, sans-serif;
    font-weight: 800; font-size: 26px; color: var(--white); text-shadow: 0 2px 4px rgba(0,0,0,0.8);
  }
  .brand { position: absolute; left: 514px; top: 1022px; display: flex; align-items: center; gap: 16px; }
  .brand-name {
    font-family: "Cinzel", "Times New Roman", serif; font-weight: 700; font-size: 25px;
    color: var(--brand-blue); white-space: nowrap;
  }
  .brand-square { width: 70px; height: 68px; background: var(--white); border-radius: 4px; }
  .footer {
    font-family: "Open Sans", Arial, sans-serif; font-weight: 700; font-size: 19px;
    color: var(--white); text-shadow: 0 2px 4px rgba(0,0,0,0.9);
  }
</style>
</head>
<body>
<main class="poster">
  <div class="stage-scene" role="img" aria-label="Red stage curtain glowing orange and magenta, a silhouetted guitarist on stage above a cheering crowd, wooden stage floor below"></div>

  <h1 class="line title">VELVET AMPS</h1>
  <h2 class="line subtitle">The Ultimate Rock Band</h2>
  <h2 class="line subtitle-dark">Course for Adults</h2>

  <p class="line intro" style="top:346px">Ever wondered what it would be like to play in a band?</p>
  <p class="line intro" style="top:377px">Feeling musically rusty and looking for a way</p>
  <p class="line intro" style="top:408px">to start playing your instrument again?</p>

  <p class="line callout" style="top:456px">Then here’s an exciting opportunity</p>
  <p class="line callout" style="top:497px">you can’t miss!</p>

  <p class="line detail" style="top:551px">All musical levels</p>
  <p class="line detail detail-strong" style="top:578px">Beginner / Intermediate to Advanced Players</p>
  <p class="line detail" style="top:627px">Limited Numbers</p>
  <p class="line detail detail-large" style="top:663px">Starts Saturday 3rd August</p>
  <p class="line detail detail-large" style="top:695px">Newtown</p>

  <p class="line small" style="top:748px">Over 6 exciting weekends you’ll work with one of our experienced professional</p>
  <p class="line small" style="top:770px">band coaches and transform yourselves into the ultimate ‘Velvet Amps’</p>

  <p class="line small" style="top:811px">Discover how to play in a band</p>
  <p class="line small" style="top:831px">Revisit your musical abilities</p>
  <p class="line small" style="top:851px">Practice songs</p>
  <p class="line small" style="top:871px">Perform on Stage</p>

  <p class="line small" style="top:905px">Drummers, Bass Guitarists, Singers, Keys, Guitarists, Saxophone, Percussionists</p>
  <p class="line small" style="top:933px">and others</p>

  <p class="line welcome">ALL WELCOME TO JOIN</p>

  <p class="register" style="top:1022px">REGISTER ONLINE NOW</p>
  <p class="register" style="top:1052px">www.tunelanestudio.com.au</p>

  <div class="brand">
    <span class="brand-name">Tunelane Studio</span>
    <span class="brand-square"></span>
  </div>

  <p class="line footer" style="top:1088px">For more information, course costs and registration,</p>
  <p class="line footer" style="top:1114px">please visit www.tunelanestudio.com.au or call 02 7194 2586 / 0472 908 645</p>
</main>
</body>
</html>
```